Corvid Lending Systems Re-design.

Corvid have recently launched a new site using Tile Frame CMS system (http://www.corvidlendingsystems.example.au). We are looking to update the look and feel to match the rest of our brands (http://www.velmora.example.au and http://www.brixline.example.au) We are keen for the design to be more visually engaging, incorporating more imagery and create a clean and easy to navigate interface.

We are looking for 2 pages to be designed. The first page would be the homepage which should contain the following:
Menu to the sub categories provided in the site map.
Room for latest news articles
Small area for polls
Contact us section
Page 2 should offer a content page. An example of this would be CRM (sales Platform) from the site map. This page would need to contain an overall description of the product and menu to the following:
Flash Demo.
Features and Benefits.
Enquire now.

Target Market(s)

Corvid offer software and web tools that enable Mortgage brokers to manage their clients, choose the most applicable loan and submit applications to the lender (bank).
The target market for this site is mainly mortgage brokers and the banking industry (lenders, Brokerages and Aggregators of homeloans).
Mortgage brokers often work in small brokerages or are self employed running their business within the local community, alternatively they may own a franchise business such as Tandell Credit Hub, KUDO or Lendwise Path.

Industry/Entity Type

Software

Number of Pages Required

2 pages

Requirements
Must have
• Must suitably match the look and feel of our sister companies velmora.example.au and brixline.example.au and our group site corvidgroup.example.au.
Colour scheme should not differ from the base logo colours provided.
Should not have
• Although Corvid offers mortgage software to brokers we do not sell homeloans or deal directly with buyers, therefore pictures of houses and a look you see from lenders is not what we are looking for. Our customers are Mortgage brokers and top tier banks.

```html
<!DOCTYPE html>
<html lang="en">
<head>
<meta charset="utf-8">
<title>Corvid — Home</title>
<link rel="stylesheet" href="https://fonts.googleapis.com/css2?family=Arimo:ital,wght@0,400;0,700;1,700&family=PT+Sans:wght@400;700&family=PT+Sans+Narrow:wght@700&display=swap">
<style>
  :root {
    --page-bg: #dcdcdc;
    --frame-border: #bdbdbd;
    --crimson: #a00000;
    --brand: #b3123f;
    --nav-active: #8e98bd;
    --heading-red: #a50d0d;
    --text: #333333;
    --muted: #7a7a7a;
    --panel-line: #cfcfcf;
  }
  * { margin: 0; padding: 0; box-sizing: border-box; }
  html, body { width: 1132px; height: 1200px; overflow: hidden; background: var(--page-bg); }
  body { font-family: "Arimo", Arial, sans-serif; color: var(--text); }
  .stage { position: relative; width: 1152px; height: 1221px; transform: scale(0.98264); transform-origin: 0 0; }
  .site-frame {
    position: absolute; left: 96px; top: 20px; width: 960px; height: 1171px;
    border: 1px solid var(--frame-border);
    background: linear-gradient(#e6e6e6 0, #f7f7f7 110px, #f6f6f6 100%);
  }
  .abs { position: absolute; }

  .logo { left: 131px; top: 38px; display: flex; align-items: center; gap: 8px;
    font-family: "PT Sans", sans-serif; font-weight: 700; color: var(--brand); }
  .logo-mark { width: 14px; height: 14px; border-radius: 50%; background: var(--brand); }
  .logo-name { font-size: 46px; line-height: 1; letter-spacing: -1px; }

  .main-nav { left: 131px; top: 119px; width: 890px; height: 31px; background: var(--crimson);
    font-family: "PT Sans", sans-serif; font-size: 13px; color: #fff; }
  .main-nav a { position: absolute; top: 7px; color: #fff; text-decoration: none; white-space: nowrap; }
  .main-nav .is-active { left: 0; top: 0; width: 85px; height: 31px; background: var(--nav-active);
    display: flex; align-items: center; justify-content: center; }
  .main-nav .is-active::after { content: ""; position: absolute; left: 37px; bottom: -7px;
    border: 6px solid transparent; border-top-color: var(--nav-active); border-bottom: 0; }

  .hero-photo { left: 131px; top: 150px; width: 380px; height: 270px;
    background: radial-gradient(ellipse at 62% 55%, #d8c3ad 0, #cfd2d8 40%, #eeeeee 75%, #f6f6f6 100%); }
  .hero-copy { left: 501px; top: 172px; width: 520px; }
  .hero-copy h1 { font-family: "PT Sans", sans-serif; font-weight: 400; font-size: 35px; color: var(--brand); line-height: 1; margin-bottom: 19px; }
  .hero-copy p { font-size: 12.5px; line-height: 17px; margin-bottom: 17px; }
  .firsts { list-style: none; margin: 22px 0 0 39px; }
  .firsts li { font-size: 11px; font-weight: 700; margin-bottom: 12px; position: relative; padding-left: 10px; }
  .firsts li::before { content: ""; position: absolute; left: 0; top: 4px; width: 4px; height: 4px; background: var(--crimson); }

  .services { left: 131px; top: 420px; width: 890px; height: 177px; border-top: 1px solid #d6d6d6;
    background: linear-gradient(#f4f4f4, #dedede); }
  .service { position: absolute; top: 28px; }
  .service svg { position: absolute; left: -29px; top: 0; }
  .service h3 { font-family: "PT Sans Narrow", sans-serif; font-size: 14px; line-height: 16px; color: var(--heading-red); letter-spacing: -0.3px; }
  .service p { font-size: 10.5px; line-height: 13.3px; color: var(--muted); margin-top: 4px; }
  .pill { display: inline-flex; align-items: center; justify-content: center; gap: 4px;
    height: 17px; padding: 0 10px; border-radius: 9px; font-size: 9px; color: #666;
    background: linear-gradient(#f6f6f6, #c9c9c9); box-shadow: 0 1px 1px rgba(0,0,0,.25); }
  .pill::after { content: ""; border: 3px solid transparent; border-left: 3px solid #666; border-right: 0; }
  .service .pill { position: absolute; left: 0; top: 107px; width: 76px; }

  .content-box { left: 131px; top: 607px; width: 890px; height: 454px; background: #fff; border: 1px solid var(--panel-line); }
  .content-box .divider { position: absolute; left: 609px; top: 0; width: 1px; height: 100%; background: var(--panel-line); }
  .intro { position: absolute; left: 19px; top: 16px; width: 552px; font-size: 12.3px; line-height: 17px; }
  .intro h2 { font-family: "PT Sans Narrow", sans-serif; font-size: 24px; color: var(--heading-red); margin-bottom: 17px; }
  .intro-photo { float: left; width: 246px; height: 86px; margin: 3px 15px 0 0;
    border: 3px solid #bdbdbd; background: linear-gradient(100deg, #8a6d4f, #c6a54a 50%, #e6d233 75%, #7d6a4d); }
  .intro p { margin-bottom: 17px; }

  .sidebar { position: absolute; left: 639px; top: 21px; width: 220px; font-size: 10.5px; line-height: 17px; }
  .side-title { position: relative; height: 31px; padding: 4px 0 0 9px; border: 1px solid #d6d6d6; border-right: 0;
    background: linear-gradient(#ffffff, #ececec); font-family: "PT Sans Narrow", sans-serif; font-size: 18px; color: var(--heading-red); }
  .side-title::after { content: ""; position: absolute; left: 22px; bottom: -6px;
    border: 6px solid transparent; border-top-color: #d6d6d6; border-bottom: 0; }
  .news { padding: 12px 0 0 10px; }
  .news h4 { font-size: 12px; font-weight: 700; color: #444; line-height: 15px; }
  .news time { display: block; font-size: 9.5px; color: #999; margin-bottom: 13px; line-height: 12px; }
  .news p { margin-bottom: 17px; }
  .news .pill { margin: -9px 0 0 124px; width: 76px; }
  .poll { margin-top: 22px; }
  .poll-body { padding: 11px 0 0 10px; }
  .poll-options { list-style: none; margin: 6px 0 8px 9px; }
  .poll-options li { display: flex; align-items: center; gap: 5px; }
  .poll-options span.radio { width: 11px; height: 11px; border-radius: 50%; border: 1px solid #999; background: linear-gradient(#fff, #ddd); }
  .poll .pill { margin-left: 9px; width: 75px; }

  .site-footer { left: 131px; top: 1071px; width: 890px; height: 89px; background: var(--crimson);
    color: #fff; text-align: center; font-size: 10.5px; padding-top: 18px; line-height: 13px; }
  .site-footer b { font-weight: 700; }
  .footer-links { margin-top: 13px; font-weight: 700; }
</style>
</head>
<body>
<div class="stage">
  <div class="site-frame"></div>

  <div class="abs logo"><span class="logo-mark"></span><span class="logo-name">corvid group</span></div>

  <nav class="abs main-nav">
    <a class="is-active" href="#">Home</a>
    <a href="#" style="left:103px">Mortgage Solutions</a>
    <a href="#" style="left:249px">Messaging</a>
    <a href="#" style="left:348px">Company</a>
    <a href="#" style="left:442px">News</a>
    <a href="#" style="left:524px">Support</a>
    <a href="#" style="left:599px">Privacy Policy</a>
    <a href="#" style="left:714px">Site Map</a>
    <a href="#" style="left:802px">Contact Us</a>
  </nav>

  <div class="abs hero-photo" role="img" aria-label="Smiling young woman giving a thumbs up in front of a celebrating office team"></div>

  <section class="abs hero-copy">
    <h1>Welcome to Corvid</h1>
    <p>Corvid is a leading software player in the Australian mortgage industry with over 10 years industry track record as a proven innovator.</p>
    <p>Corvid has been responsible for numerous industry firsts in the evolution of its suite of tools and services to mortgage industry professionals including:</p>
    <ul class="firsts">
      <li>First 3rd party electronic application platform based on LXDS (2003)</li>
      <li>First direct to consumer LXDS based online application (2006)</li>
      <li>First 'built for industry' product data hub (2009)</li>
    </ul>
  </section>

  <section class="abs services">
    <div class="service" style="left:38px;width:130px">
      <svg width="22" height="22" viewBox="0 0 22 22"><rect x="3" y="5" width="16" height="14" rx="2" fill="#e2b64a" stroke="#8a6a1f"/><circle cx="11" cy="12" r="4" fill="#fff" stroke="#8a6a1f"/></svg>
      <h3>CRM (Sales Platform)</h3>
      <p>Lorem ipsum dolor sit amet, consectetur adipiscing elit. Curabitur ligula ipsum, dapibus non aliquet in, rutrum eu tellus.</p>
      <span class="pill">learn more</span>
    </div>
    <div class="service" style="left:218px;width:130px">
      <svg width="22" height="22" viewBox="0 0 22 22"><circle cx="11" cy="11" r="8" fill="#dfe8f5" stroke="#3d6fb6" stroke-width="2"/><path d="M7 11h8M12 8l3 3-3 3" fill="none" stroke="#3d6fb6" stroke-width="1.6"/></svg>
      <h3>Commission Processing</h3>
      <p>Lorem ipsum dolor sit amet, consectetur adipiscing elit. Curabitur ligula ipsum, dapibus non aliquet in, rutrum eu tellus.</p>
      <span class="pill">learn more</span>
    </div>
    <div class="service" style="left:393px;width:150px">
      <svg width="22" height="22" viewBox="0 0 22 22"><path d="M3 19L19 3M3 3l16 16" stroke="#5c7fa8" stroke-width="3" stroke-linecap="round"/></svg>
      <h3>Electronic Lodgement (E-App) and Application Tracking</h3>
      <p>Lorem ipsum dolor sit amet, consectetur adipiscing elit. Curabitur ligula ipsum, dapibu.</p>
      <span class="pill">learn more</span>
    </div>
    <div class="service" style="left:589px;width:125px">
      <svg width="22" height="22" viewBox="0 0 22 22"><rect x="3" y="2" width="13" height="17" fill="#fff" stroke="#888"/><circle cx="13" cy="13" r="4" fill="none" stroke="#3d6fb6" stroke-width="2"/><path d="M16 16l4 4" stroke="#3d6fb6" stroke-width="2"/></svg>
      <h3>Mortgage Product Search and Compare</h3>
      <p>Lorem ipsum dolor sit amet, consectetur adipiscing elit. Curabitur ligula ipsum, dapibus.</p>
      <span class="pill">learn more</span>
    </div>
    <div class="service" style="left:748px;width:130px">
      <svg width="22" height="22" viewBox="0 0 22 22"><rect x="4" y="2" width="14" height="18" rx="1" fill="#666"/><rect x="6" y="4" width="10" height="4" fill="#cfd8c4"/><g fill="#ddd"><rect x="6" y="10" width="2.5" height="2"/><rect x="10" y="10" width="2.5" height="2"/><rect x="14" y="10" width="2" height="2"/><rect x="6" y="14" width="2.5" height="2"/><rect x="10" y="14" width="2.5" height="2"/><rect x="14" y="14" width="2" height="2"/></g></svg>
      <h3>Mortgage Calculators</h3>
      <p>Lorem ipsum dolor sit amet, consectetur adipiscing elit. Curabitur ligula ipsum, dapibus non aliquet in, rutrum eu tellus.</p>
      <span class="pill">learn more</span>
    </div>
  </section>

  <main class="abs content-box">
    <div class="divider"></div>
    <article class="intro">
      <h2>Intro Heading Text</h2>
      <div class="intro-photo" role="img" aria-label="Team meeting around a table in a bright yellow office"></div>
      <p><b><i>Corvid is a leading software player in the Australian mortgage industry with over 10 years industry track record as a proven innovator.</i></b> Corvid has been responsible for numerous industry firsts in the evolution of its suite of tools and services to mortgage industry professionals including. Corvid is a leading software player in the Australian mortgage industry with over 10 years industry track record as a proven innovator. Corvid has been responsible for numerous industry firsts in the evolution of its suite of tools and services to mortgage industry professionals including.</p>
      <p>Corvid is a leading software player in the Australian mortgage industry with over 10 years industry track record as a proven innovator. Corvid has been responsible for numerous industry firsts in the evolution of its suite of tools and services to mortgage industry professionals including. Corvid is a leading software player in the Australian mortgage industry with over 10 years industry track record as a proven innovator. Corvid has been responsible for numerous industry firsts in the evolution of its suite of tools and services to mortgage industry professionals including. Corvid is a leading software player in the Australian mortgage industry with over 10 years.</p>
      <p>Corvid is a leading software player in the Australian mortgage industry with over 10 years industry track record as a proven innovator. Corvid has been responsible for numerous industry firsts in the evolution of its suite of tools and services to mortgage industry professionals including. Corvid is a leading software player in the Australian mortgage industry with over 10 years.</p>
    </article>

    <aside class="sidebar">
      <div class="side-title">Latest News &amp; Articles</div>
      <div class="news">
        <h4>Corvid Names New GM</h4>
        <time>Thursday, December 3, 2009 at 3:31PM</time>
        <p>Corvid has appointed Martin Hale as the company’s new general manager.</p>
        <p>Mr Hale, who has been a part of the Corvid group since its inception, has held the position of business manager for the past few years.</p>
        <span class="pill">read more</span>
      </div>
      <div class="poll">
        <div class="side-title">Poll</div>
        <div class="poll-body">
          <p>Corvid has appointed Martin Hale as the company’s new general manager?</p>
          <ul class="poll-options">
            <li><span class="radio"></span>Best</li>
            <li><span class="radio"></span>Better</li>
            <li><span class="radio"></span>Worst</li>
          </ul>
          <span class="pill">submit</span>
        </div>
      </div>
    </aside>
  </main>

  <footer class="abs site-footer">
    <p><b>Office Location:</b> Level 14 62 Harbour Lane Northpoint NSW 2199 &nbsp;| &nbsp;<b>Sales:</b> 02 9000 4812 &nbsp;| &nbsp;<b>Support:</b> 1300 555 208</p>
    <p class="footer-links">Sales Platform | e-app | Product Engine | Calculations | Commissions | Messaging | IT Services | Support | Company | News | Contact</p>
    <p>© 2009, Corvid Group Inc. All rights reserved.</p>
  </footer>
</div>
</body>
</html>
```